Small Business coaching and services company

Need a powerpoint template design for a company that provides Human Resources services as well sales and business coaching.

```html
<!DOCTYPE html>
<html lang="en">
<head>
<meta charset="utf-8">
<title>GrowPoint – Title Slide</title>
<link href="https://fonts.googleapis.com/css2?family=Open+Sans:wght@400;600;700&display=swap" rel="stylesheet">
<style>
  :root {
    --bg-deep: #141414;
    --bg-mid: #242424;
    --bg-light: #2e2e2e;
    --text-main: #f4f4f4;
    --text-soft: #d6d6d6;
    --accent-gold: #f5a800;
    --accent-purple: #6a3a9c;
  }
  * { margin: 0; padding: 0; box-sizing: border-box; }
  html, body {
    width: 1200px;
    height: 667px;
    overflow: hidden;
    background: var(--bg-deep);
  }
  .slide {
    position: relative;
    width: 1200px;
    height: 667px;
    overflow: hidden;
    font-family: "Open Sans", Arial, sans-serif;
    color: var(--text-main);
  }
  .slide-backdrop {
    position: absolute;
    inset: 0;
    background:
      radial-gradient(ellipse 55% 45% at 45% 62%, #2f2f2f 0%, rgba(40,40,40,0) 70%),
      radial-gradient(ellipse 40% 35% at 80% 20%, #2c2c2c 0%, rgba(40,40,40,0) 70%),
      linear-gradient(160deg, var(--bg-deep) 0%, var(--bg-mid) 55%, #1a1a1a 100%);
  }
  .brand {
    position: absolute;
    top: 190px;
    left: 0;
    width: 100%;
    display: flex;
    justify-content: center;
    align-items: center;
    gap: 16px;
  }
  .brand-mark {
    width: 62px;
    height: 62px;
    border-radius: 50%;
    background: var(--accent-purple);
  }
  .brand-name {
    font-size: 52px;
    font-weight: 700;
    color: var(--accent-gold);
    letter-spacing: -1px;
    line-height: 1;
  }
  .title {
    position: absolute;
    top: 290px;
    width: 100%;
    text-align: center;
    font-size: 42px;
    font-weight: 700;
    letter-spacing: 0.3px;
  }
  .subtitle {
    position: absolute;
    top: 357px;
    width: 100%;
    text-align: center;
    font-size: 22px;
    font-weight: 400;
    color: var(--text-soft);
    letter-spacing: 0.3px;
  }
  .presenter {
    position: absolute;
    top: 461px;
    width: 100%;
    text-align: center;
    font-size: 26px;
    font-weight: 700;
  }
  .presenter-surname { color: var(--accent-gold); }
  .footer-date, .footer-site {
    position: absolute;
    top: 605px;
    font-size: 17px;
    font-weight: 400;
  }
  .footer-date { left: 57px; }
  .footer-site { right: 57px; top: 603px; }
</style>
</head>
<body>
  <main class="slide">
    <div class="slide-backdrop" role="img" aria-label="Darkened photo of a business meeting: laptops, coffee cup and potted plant on a round table"></div>

    <div class="brand">
      <span class="brand-mark"></span>
      <span class="brand-name">GrowPoint</span>
    </div>

    <h1 class="title">Presentation Tittle Goes Here</h1>
    <p class="subtitle">Credential Subtittle Presentation</p>

    <p class="presenter">Mr. Daniel <span class="presenter-surname">Okoro</span></p>

    <p class="footer-date">February 2023</p>
    <p class="footer-site">website.com</p>
  </main>
</body>
</html>
```